K. Morendi needs an original business card for property investment professionals

The business card would be to present me as an investor in the real estate business. The market are developers of real estate projects, or other people who would like to sell and also to give us a name as a company. For style, colour and imagery I would like something artistic from Morendi (the artist) with a different touch.

Address, email, cel phone,
Updates

Hi¡ Update¡ I;d like it to stop providing Bright Acre as a Design and focus in K.Morendi.

Target Market(s)

Real Estate Developer/Investor

Industry/Entity Type

Real Estate

Colors
33a6d7
886aae
e3daeb
cadf82
f78f20

```html
<!DOCTYPE html>
<html lang="en">
<head>
<meta charset="UTF-8">
<title>K. Morendi — Business Card</title>
<link rel="stylesheet" href="https://fonts.googleapis.com/css2?family=Poppins:wght@500;600&display=swap">
<style>
  :root {
    --stage: #e6e6e4;
    --card: #f7f7f6;
    --sky: #72bfe1;
    --accent: #33a6d7;
    --ink: #4d4d4f;
  }
  * { box-sizing: border-box; margin: 0; padding: 0; }
  html, body {
    width: 1200px;
    height: 1000px;
    overflow: hidden;
    background: var(--stage);
  }
  .stage {
    position: relative;
    width: 1200px;
    height: 1000px;
  }
  .card {
    position: absolute;
    top: 220px;
    width: 360px;
    height: 560px;
    background: var(--card);
    box-shadow: 0 2px 6px rgba(0,0,0,0.12);
    overflow: hidden;
  }
  .card--front { left: 180px; }
  .card--back { left: 660px; }
  .card__shape {
    position: absolute;
    inset: 0;
    width: 100%;
    height: 100%;
  }
  .brand {
    position: absolute;
    left: 34px;
    top: 150px;
    display: flex;
    align-items: center;
    gap: 10px;
    font-family: "Poppins", sans-serif;
    font-weight: 600;
    font-size: 44px;
    letter-spacing: 0.5px;
    color: var(--ink);
  }
  .brand__dot {
    width: 14px;
    height: 14px;
    border-radius: 50%;
    background: var(--accent);
  }
  .contact {
    position: absolute;
    right: 28px;
    bottom: 70px;
    text-align: right;
    font-family: "Poppins", sans-serif;
    font-weight: 600;
    font-size: 17px;
    line-height: 1.55;
    color: var(--ink);
    list-style: none;
  }
</style>
</head>
<body>
<main class="stage">
  <section class="card card--front" aria-label="Card front">
    <svg class="card__shape" viewBox="0 0 360 560" preserveAspectRatio="none" aria-hidden="true">
      <polygon points="0,0 78,0 52,34" fill="var(--sky)"/>
    </svg>
    <div class="brand">
      <span class="brand__dot" aria-hidden="true"></span>
      <span class="brand__name">K.Morendi</span>
    </div>
    <ul class="contact">
      <li>morendimail@mail.com</li>
      <li>Tel.no.:445-7826</li>
      <li>www.morendi-invest.com</li>
    </ul>
  </section>

  <section class="card card--back" aria-label="Card back">
    <svg class="card__shape" viewBox="0 0 360 560" preserveAspectRatio="none" aria-hidden="true">
      <polygon points="0,0 250,0 345,505" fill="var(--sky)"/>
    </svg>
  </section>
</main>
</body>
</html>
```